Need design for Vinyl window signs

I need Vinyl window sign to cover my front retail pharmacy window. Not the whole window area i want there to be open areas so people can still see inside.
Attached is the pic of front door and also the logo which contains the colors we want to use. The width of the door is about 14ft wide and 7ft high and its 3 sections. The middle section the door is 36 inch.

And the vinyl graphic should include the following info:
Maplecrest Commons pharmacy
Caring for you, Caring for the community

Wellness starts here!
Locally owned independent pharmacy
No wait
Same Copay as chains
Free local delivery

We do prescriptions, private consultations, compounding, immunizations, travel health and other clinical services

We also provide free blood pressure, blood glucose and blood oxygen testing everyday.
No appointments necessary.

Write Pharmacy in different languages: Spanish, Farsi, Hebrew, Russian

Phone: 555-206-3948

Hours:
M- F 9-6
Sat and sun and major Holliday: closed

Target Market(s)

Patients: People seeking medication or health advice. Caregivers: Those caring for others who need prescriptions. Health-Conscious Individuals: People interested in preventive health measures. Chronic Condition Sufferers: Individuals managing ongoing health issues. Healthcare Professionals: Doctors and nurses who may refer patients to pharmacists.

Industry/Entity Type

Retail pharmacy

Font styles to use
Sans Serif

Colors
0054AA
0677BA
7BADD7
CADEEF
E8F1F8
00AB8E
00BBA5
67D7C9
C6EFE9
E9F9F6

Requirements
Must have
• At least 3 sections for each window left side and right side and middle area, must have Green and blue color to match my logo see attached.
Nice to have
• Like to see a pics or two of people maybe seniors and younger adults enjoying their time

```html
<!DOCTYPE html>
<html lang="en">
<head>
<meta charset="utf-8">
<title>Maplecrest Commons Pharmacy – Window Signs</title>
<link rel="stylesheet" href="https://fonts.googleapis.com/css2?family=Anton&family=Montserrat:wght@600;700;800&family=Oswald:wght@500;600&display=swap">
<style>
  :root{
    --bg:#1c1c1c;
    --blue:#0b5eb4;
    --green:#1fc44b;
    --navy:#123f8e;
    --white:#ffffff;
    --photo-a:#6f9a4a;
    --photo-b:#c9b28e;
    --photo-c:#8fb86a;
  }
  *{margin:0;padding:0;box-sizing:border-box}
  html,body{width:1200px;height:1200px;overflow:hidden;background:var(--bg)}
  .canvas{position:relative;width:1200px;height:1200px;display:flex;gap:60px;justify-content:center;align-items:center}
  .sign{position:relative;width:470px;height:1080px;background:var(--blue);overflow:hidden;color:var(--white);font-family:"Montserrat",sans-serif}

  .brand{position:absolute;left:0;top:0;width:100%;height:166px;display:flex;align-items:center;padding-left:28px;gap:16px}
  .brand-dot{width:96px;height:96px;border-radius:50%;background:var(--white);flex:none}
  .brand-name{font-weight:800;font-size:25px;line-height:1.12;letter-spacing:.2px}
  .brand-langs{font-family:"Oswald",sans-serif;font-weight:500;font-size:10.5px;letter-spacing:.3px;margin-top:6px}
  .stripe{position:absolute;left:0;width:100%;height:9px;background:var(--green)}
  .stripe.top{top:166px}
  .stripe.mid{top:498px}
  .photo{position:absolute;left:0;top:180px;width:100%;height:318px}
  .photo.family{background:linear-gradient(160deg,var(--photo-a) 0%,var(--photo-b) 55%,var(--photo-c) 100%)}
  .photo.seniors{background:linear-gradient(170deg,#a9c98d 0%,#d8c7b0 45%,#7fae5b 100%)}

  .headline{position:absolute;top:520px;width:100%;text-align:center;font-weight:800;font-size:43px;line-height:1}
  .headline .accent{display:block;color:var(--green);margin-top:2px}
  .rule{position:absolute;top:612px;left:145px;width:180px;height:3px;background:var(--white)}
  .perks{position:absolute;top:635px;left:25px;list-style:none;font-family:"Oswald",sans-serif;font-weight:500;font-size:21px;letter-spacing:.2px}
  .perks li{display:flex;align-items:center;gap:9px;height:37px}
  .tick{width:17px;height:17px}

  .footer{position:absolute;left:0;bottom:0;width:100%;height:300px}
  .footer svg.edge{position:absolute;top:0;left:0}
  .phone{position:absolute;top:52px;width:100%;display:flex;justify-content:center;align-items:center;gap:6px;font-family:"Oswald",sans-serif;font-weight:600;font-size:62px;color:var(--navy);line-height:1}
  .phone svg{width:40px;height:40px}
  .hours{position:absolute;top:138px;width:100%;text-align:center;font-weight:800;font-size:33px;line-height:1}
  .closed{position:absolute;top:176px;width:100%;text-align:center;font-weight:700;font-size:15.5px}
  .pill{position:absolute;left:34px;right:34px;background:var(--navy);border-radius:10px;text-align:center;color:var(--white)}
  .pill.appt{top:210px;height:44px;font-family:"Oswald",sans-serif;font-weight:500;font-size:27px;line-height:44px}

  .services-title{position:absolute;top:530px;width:100%;text-align:center;font-weight:700;font-size:23px;letter-spacing:.6px}
  .services{position:absolute;top:580px;left:30px;display:grid;grid-template-columns:212px 200px;row-gap:17px}
  .service{display:flex;align-items:center;gap:10px;font-weight:700;font-size:18px;line-height:1.1;height:56px}
  .service .icon{width:56px;height:56px;flex:none;border-radius:50%;border:2px solid var(--white);background:var(--green);display:flex;align-items:center;justify-content:center}
  .service .icon svg{width:30px;height:30px}

  .free{position:absolute;top:55px;width:100%;text-align:center;font-family:"Anton",sans-serif;font-size:72px;line-height:1.02;color:var(--white)}
  .free .accent{color:var(--navy)}
  .pill.tests{top:222px;left:26px;right:26px;padding:6px 4px;font-weight:800;font-size:15.5px;line-height:1.2}
</style>
</head>
<body>
<main class="canvas">

  <!-- Wellness sign -->
  <section class="sign sign-wellness">
    <header class="brand">
      <span class="brand-dot"></span>
      <div>
        <div class="brand-name">MAPLECREST COMMONS<br>PHARMACY</div>
        <div class="brand-langs">FARMACIA | DARUKHANEH | BEIT MERKACHAT | APTEKA</div>
      </div>
    </header>
    <div class="stripe top"></div>
    <div class="photo family" role="img" aria-label="Photo of a smiling young family of four outdoors in a sunny park"></div>
    <div class="stripe mid"></div>

    <h2 class="headline">WELLNESS<span class="accent">STARTS HERE!</span></h2>
    <div class="rule"></div>
    <ul class="perks">
      <li><svg class="tick" viewBox="0 0 20 20"><circle cx="10" cy="10" r="8.5" fill="none" stroke="#fff" stroke-width="1.8"/><path d="M6 10.3l2.7 2.7L14.2 7.3" fill="none" stroke="#fff" stroke-width="1.8"/></svg>LOCALLY OWNED INDEPENDENT PHARMACY</li>
      <li><svg class="tick" viewBox="0 0 20 20"><circle cx="10" cy="10" r="8.5" fill="none" stroke="#fff" stroke-width="1.8"/><path d="M6 10.3l2.7 2.7L14.2 7.3" fill="none" stroke="#fff" stroke-width="1.8"/></svg>NO WAIT</li>
      <li><svg class="tick" viewBox="0 0 20 20"><circle cx="10" cy="10" r="8.5" fill="none" stroke="#fff" stroke-width="1.8"/><path d="M6 10.3l2.7 2.7L14.2 7.3" fill="none" stroke="#fff" stroke-width="1.8"/></svg>SAME COPAY AS CHAINS</li>
      <li><svg class="tick" viewBox="0 0 20 20"><circle cx="10" cy="10" r="8.5" fill="none" stroke="#fff" stroke-width="1.8"/><path d="M6 10.3l2.7 2.7L14.2 7.3" fill="none" stroke="#fff" stroke-width="1.8"/></svg>FREE LOCAL DELIVERY</li>
    </ul>

    <footer class="footer">
      <svg class="edge" width="470" height="300" viewBox="0 0 470 300">
        <polygon points="0,8 235,44 470,8 470,300 0,300" fill="var(--green)"/>
        <polyline points="0,0 235,36 470,0" fill="none" stroke="#fff" stroke-width="4"/>
      </svg>
      <div class="phone">
        <svg viewBox="0 0 24 24"><path d="M6.6 2.5l3 3.4-1.8 2.6c1 2.3 3.1 4.6 5.6 5.8l2.6-1.8 3.5 3-1.5 3.6C11 18.9 5 12.8 3 6z" fill="#fff"/><path d="M14 3.5a6.5 6.5 0 0 1 6.5 6.5M14 6.5A3.5 3.5 0 0 1 17.5 10" fill="none" stroke="#fff" stroke-width="1.8"/></svg>
        555-206-3948
      </div>
      <div class="hours">MON - FRI : 9AM - 6PM</div>
      <div class="closed">SAT AND SUN AND MAJOR HOLIDAY: CLOSED</div>
      <div class="pill appt">NO APPOINTMENTS NECESSARY.</div>
    </footer>
  </section>

  <!-- Services sign -->
  <section class="sign sign-services">
    <header class="brand">
      <span class="brand-dot"></span>
      <div>
        <div class="brand-name">MAPLECREST COMMONS<br>PHARMACY</div>
        <div class="brand-langs">FARMACIA | DARUKHANEH | BEIT MERKACHAT | APTEKA</div>
      </div>
    </header>
    <div class="stripe top"></div>
    <div class="photo seniors" role="img" aria-label="Photo of four cheerful senior friends walking on a golf course carrying golf bags"></div>
    <div class="stripe mid"></div>

    <h2 class="services-title">SERVICES PROVIDED</h2>
    <div class="services">
      <div class="service"><span class="icon"><svg viewBox="0 0 24 24" fill="none" stroke="#fff" stroke-width="1.6"><rect x="5" y="3" width="14" height="18" rx="1.5"/><path d="M9 8h6M9 12l3 3 3-5"/></svg></span>Prescriptions</div>
      <div class="service"><span class="icon"><svg viewBox="0 0 24 24" fill="none" stroke="#fff" stroke-width="1.6"><rect x="3" y="4" width="18" height="13" rx="1.5"/><circle cx="12" cy="10" r="2.5"/><path d="M8 21h8M12 17v4"/></svg></span>Private<br>Consultations</div>
      <div class="service"><span class="icon"><svg viewBox="0 0 24 24" fill="none" stroke="#fff" stroke-width="1.6"><path d="M4 12h16a8 8 0 0 1-16 0zM14 12l6-8"/></svg></span>Compounding</div>
      <div class="service"><span class="icon"><svg viewBox="0 0 24 24" fill="none" stroke="#fff" stroke-width="1.6"><path d="M15 3l6 6M18 6l-9 9-3 0 0-3 9-9M6 18l-3 3M11 9l2 2"/></svg></span>Immunizations</div>
      <div class="service"><span class="icon"><svg viewBox="0 0 24 24" fill="none" stroke="#fff" stroke-width="1.6"><path d="M12 21s-6-6-6-11a6 6 0 0 1 12 0c0 5-6 11-6 11z"/><circle cx="12" cy="10" r="2.3"/></svg></span>Travel Health</div>
    </div>

    <footer class="footer">
      <svg class="edge" width="470" height="300" viewBox="0 0 470 300">
        <polygon points="0,8 235,44 470,8 470,300 0,300" fill="var(--green)"/>
        <polyline points="0,0 235,36 470,0" fill="none" stroke="#fff" stroke-width="4"/>
      </svg>
      <div class="free">WE ALSO<br>PROVIDE <span class="accent">FREE</span></div>
      <div class="pill tests">BLOOD PRESSURE, BLOOD GLUCOSE AND<br>BLOOD OXYGEN TESTING EVERYDAY.</div>
    </footer>
  </section>

</main>
</body>
</html>
```